Verpackungsdesign für Parfüm gesucht
Zielgruppe
Wir werden eine Marke unter dem Namen ORMAL mit Parfüm auf dem Markt bringen und benötigen hierfür ein hochwertiges Design . Unsre Zielgruppe ist m/w/d und zwischen 16 und 60 Jahre.
Aufgabenstellung
Bei der Verpackung handelt es sich um eine Schiebeschachtel. Wir benötigen das Design nur für die Außenhülle, nicht für den Schuber.
Pflichtangaben auf der Verpackung sind unser Logo, Eau de Parfum, High Intense, 20 ml e 0.67 FL OZ,
Natural Spray Vaporisateur,

```html
<!DOCTYPE html>
<html lang="en">
<head>
<meta charset="utf-8">
<title>ORMAL Eau de Parfum – Outer Sleeve</title>
<link rel="stylesheet" href="https://fonts.googleapis.com/css2?family=EB+Garamond:wght@400;500;600&display=swap">
<style>
  :root {
    --backdrop: #b4b2b3;
    --sleeve-dark: #231f1e;
    --sleeve-mid: #2f2b29;
    --sleeve-light: #4e4a47;
    --side-dark: #1e1b1a;
    --ink-light: #d9d7d5;
    --ink-soft: #c9c7c5;
    --band-white: #f1f1f0;
    --band-shade: #d6d6d5;
    --band-ink: #1f1c1b;
  }
  * { margin: 0; padding: 0; box-sizing: border-box; }
  html, body {
    width: 1200px;
    height: 960px;
    overflow: hidden;
    background: var(--backdrop);
    font-family: "EB Garamond", Georgia, serif;
  }
  .sleeve {
    position: absolute;
    left: 340px;
    top: 50px;
    width: 520px;
    height: 860px;
    display: flex;
  }
  .sleeve-side {
    position: relative;
    width: 140px;
    height: 100%;
    background: var(--side-dark);
    overflow: hidden;
  }
  .side-name {
    position: absolute;
    left: 50%;
    top: 50%;
    transform: translate(-50%, -50%) rotate(90deg);
    font-size: 172px;
    font-weight: 400;
    letter-spacing: 0.04em;
    line-height: 1;
    color: var(--ink-soft);
    white-space: nowrap;
  }
  .sleeve-front {
    position: relative;
    width: 380px;
    height: 100%;
    background: linear-gradient(90deg, var(--sleeve-dark) 0%, var(--sleeve-mid) 45%, var(--sleeve-light) 100%);
    color: var(--ink-light);
    text-align: center;
  }
  .brand-name {
    position: absolute;
    top: 170px;
    left: 0;
    right: 0;
    font-size: 92px;
    font-weight: 400;
    letter-spacing: 0.06em;
    line-height: 1;
    color: var(--ink-light);
  }
  .spray-label {
    position: absolute;
    top: 385px;
    left: 0;
    right: 0;
    font-size: 27px;
    line-height: 1.35;
  }
  .divider {
    position: absolute;
    top: 472px;
    left: 50%;
    width: 32px;
    margin-left: -16px;
    height: 2px;
    background: var(--ink-light);
  }
  .concentration {
    position: absolute;
    top: 492px;
    left: 0;
    right: 0;
    font-size: 30px;
    font-weight: 500;
  }
  .intensity-band {
    position: absolute;
    top: 610px;
    left: 0;
    right: 0;
    height: 70px;
    background: linear-gradient(90deg, var(--band-shade) 0%, var(--band-white) 40%, var(--band-white) 100%);
    color: var(--band-ink);
    font-size: 32px;
    font-weight: 600;
    line-height: 70px;
  }
  .band-rule {
    position: absolute;
    left: 0;
    right: 0;
    background: var(--band-white);
  }
  .band-rule.thick { top: 688px; height: 4px; }
  .band-rule.thin { top: 698px; height: 2px; }
  .volume-metric {
    position: absolute;
    top: 735px;
    right: 26px;
    font-size: 27px;
  }
  .volume-imperial {
    position: absolute;
    top: 785px;
    left: 26px;
    font-size: 27px;
  }
</style>
</head>
<body>
  <div class="sleeve">
    <div class="sleeve-side">
      <span class="side-name">ORMAL</span>
    </div>
    <div class="sleeve-front">
      <h1 class="brand-name">ORMAL</h1>
      <p class="spray-label">Natural Spray<br>Vaporisateur</p>
      <span class="divider"></span>
      <p class="concentration">Eau de Parfum</p>
      <div class="intensity-band">High Intense</div>
      <span class="band-rule thick"></span>
      <span class="band-rule thin"></span>
      <p class="volume-metric">20 ML</p>
      <p class="volume-imperial">0.67 FL OZ</p>
    </div>
  </div>
</body>
</html>
```